College Prep Class needs logo and basic website

I am creating a prep class for students before they enter college. The class is designed to help them prepare for the EQ challenges of college life.

I am starting from scratch and am looking to create a basic website that has an About section, Program information, Contact Info and Sign up. It doesn't necessarily have to collect payments online but if it can that would be an added bonus. Or the ability to add that functionality in the future is key.

I am also looking to create logo for the course as well.

I've attached a rough layout of what I'm looking for. However I'm hoping to find someone with creative talents that can build upon this or come up with something clean, easy to use and inviting.

Industry/Entity Type

College

```html
<!DOCTYPE html>
<html lang="en">
<head>
<meta charset="utf-8">
<title>reach far: 7 keys college edition</title>
<link rel="stylesheet" href="https://fonts.googleapis.com/css2?family=Handlee&family=Noto+Sans:wght@400&display=swap">
<style>
  :root {
    --ink: #4a4a55;
    --heading: #55555e;
    --banner-bg: #000000;
    --banner-text: #f2b95c;
    --brand: #5b3fe0;
    --band-top: #fff5d6;
    --band-bottom: #fffcf2;
    --band-line: #f6e4a4;
    --card: #ffffff;
    --btn-dark: #2a16b8;
    --btn-light: #7f74ff;
  }
  * { box-sizing: border-box; margin: 0; padding: 0; }
  html, body { width: 1200px; height: 840px; overflow: hidden; background: #fff; }
  body { position: relative; font-family: "Noto Sans", Verdana, sans-serif; color: var(--ink); }

  .brand-mark {
    position: absolute; left: 62px; top: 30px; width: 234px; height: 154px;
    background: var(--banner-bg);
    display: flex; align-items: center; justify-content: center; gap: 12px;
  }
  .brand-mark .dot { width: 16px; height: 16px; border-radius: 50%; background: var(--brand); }
  .brand-mark .name { font-family: "Noto Sans", Verdana, sans-serif; font-size: 36px; color: var(--brand); }

  .title-banner {
    position: absolute; left: 630px; top: 30px; width: 510px; height: 70px;
    background: var(--banner-bg);
    display: flex; align-items: center; justify-content: center;
    font-family: "Handlee", cursive; font-size: 33px; color: var(--banner-text); letter-spacing: 0.5px;
  }

  .main-nav { position: absolute; top: 118px; left: 0; width: 1200px; height: 70px; }
  .nav-item {
    position: absolute; transform: translateX(-50%);
    display: flex; flex-direction: column; align-items: center; gap: 6px;
    font-family: "Handlee", cursive; font-size: 24px; color: var(--heading); text-decoration: none;
  }
  .nav-item .btn {
    width: 66px; height: 31px; border-radius: 8px;
    background: linear-gradient(to bottom, var(--btn-light), var(--btn-dark) 45%, var(--btn-dark) 70%, var(--btn-light));
    box-shadow: 2px 3px 4px rgba(0,0,0,0.35);
    position: relative;
  }
  .nav-item .btn::after {
    content: ""; position: absolute; left: 8px; right: 8px; top: 13px; height: 3px;
    background: #fff; border-radius: 2px; opacity: 0.9;
  }

  .content-band {
    position: absolute; left: 0; top: 208px; width: 1200px; height: 560px;
    background: linear-gradient(to bottom, var(--band-top), var(--band-bottom));
    border-top: 3px solid var(--band-line); border-bottom: 3px solid var(--band-line);
  }
  .card {
    position: absolute; top: 266px; width: 510px; height: 452px;
    background: var(--card);
    box-shadow: 3px 4px 7px rgba(0,0,0,0.28);
    font-size: 14.6px; line-height: 18.6px;
  }
  .card.about { left: 60px; padding: 47px 40px 0 50px; }
  .card.challenges { left: 630px; padding: 52px 40px 0 59px; }
  .card h1 { font-weight: 400; font-size: 20px; color: var(--heading); text-align: center; margin-bottom: 22px; }
  .card p { margin-bottom: 18px; }
  .challenge-list { list-style: none; margin: 22px 0 0 127px; }
  .challenge-list li { margin-bottom: 18.6px; position: relative; }
  .challenge-list li::before { content: "•"; position: absolute; left: -13px; }
</style>
</head>
<body>
  <div class="brand-mark"><span class="dot"></span><span class="name">reach far</span></div>
  <div class="title-banner">reach far: 7 keys college edition</div>

  <nav class="main-nav">
    <a class="nav-item" href="#" style="left:665px">program info<span class="btn"></span></a>
    <a class="nav-item" href="#" style="left:889px">sign-up/pay<span class="btn"></span></a>
    <a class="nav-item" href="#" style="left:1105px">contact<span class="btn"></span></a>
  </nav>

  <div class="content-band"></div>

  <section class="card about">
    <h1>college prep classes</h1>
    <p>Created and taught by Sam Moretti, former Resident Assistant (RA) at Front Range State University, where he was the RA for 30 students on his coed floor.</p>
    <p>Following the principles of Dana Whitfield’s <em>7 Keys of Purposeful Living</em>, Sam leads future college students to prepare for the stresses and pressures of a college lifestyle.</p>
    <p>As a Resident Assistant and student of the college experience, Sam Moretti has identified some of the common pitfalls that can lead intelligent and talented high school students to struggle with the transition to college.&nbsp; These students do not lack the IQ to be very successful in college, however struggle with the EQ challenges presents in college life.</p>
  </section>

  <section class="card challenges">
    <p>These challenges include:</p>
    <ul class="challenge-list">
      <li>A new living environment</li>
      <li>Being away from home and family</li>
      <li>Decision-making</li>
      <li>Social pressures</li>
      <li>Academic format &amp; academic goals</li>
      <li>Regulating health, food &amp; exercise</li>
      <li>Other major life events or changes</li>
    </ul>
  </section>
</body>
</html>
```